Label Wanted For New, Millennial, Hard Apple Cider Brand

California, alcoholic apple cider brand targeted towards Millennials needs a label to show product as:

Hand-crafted. Modern. Hipster. Produced from apples. Delicious. Unisex.

We are primarily a small wine producer (500cs/year - 20 barrels/year). Check the attachments for one of our current labels. Lanternfall will be the name of our cider.

This is the first release of our cider. This cider bottle we will be using is attached (Champagne Mold with a Crown Cap).

We will have several flavors over the course of the next few years and need a placeholder on the front label for the specific style:
"Off-Dry" (Tart + a Little Sweet)
"Dry" (Crisp + Tart)
"Hopped" (Fermented with Hopps)
"HoneyBee" (Fermented with Honey)
"Barrel Aged" (Aged in Barrel)
"Cross Culture" (Fermented with Wine Yeast and Viognier), etc.

Looking for a label that is modern, but also somewhat rustic. Please view our "Labels We Like" file. Something creative and different. Definitely more on the hipster side of things than old-fashioned.

Project Deadline Extended Reason: Hi designers,We are postponing the deadline due to the holidays. We've been unable to provide effective feedback to many of you with the craziness of Christmas Eve, Christmas and now New Years! Thank you for your patience. We will have feedback for many of you tomorrow and final selections on January 02. Thank you for all of your hard work. - Nell Added Friday, December 26, 2014

Target Market(s)

26-44yr old, educated, outdoorsy, food/wine loving, beer/wine/spirit drinking adults. Unisex product - should be slightly more masculine than feminine.

Industry/Entity Type

Product

Font styles to use
Decorative

Requirements
Must have
• Front:
• 1. Front Label Measurements: Maintain a 4(w) x 4.125(h) inch front with 1/4in bleed.
• 2. Font used for brand name "Lanternfall" should be legible but unique.
• 3. Artwork should be unisex. Modern with a handcrafted look.
• 4. Front Label Must Contain the Following Info:
• a. "Alc / Vol 7.0%"
• b. California Hard Apple Cider
• c. Placeholder for style of cider (DRY, HOPPED, OFF-DRY, etc.)
• Back Label:
• 1. Back Label Measurements: Maintain a 3(w) x 4.125(h) inch back w/ 1/4in bleed. One back label will be used for all ciders
• 2. Back Label Must Contain the Following Info:
• a. "GOVERNMENT WARNING: (1) ACCORDING TO THE SURGEON GENERAL, WOMEN SHOULD NOT DRINK ALCOHOLIC BEVERAGES DURING PREGNANCY BECAUSE OF THE RISK OF BIRTH DEFECTS. (2) CONSUMPTION OF ALCOHOLIC BEVERAGES IMPAIRS YOUR ABILITY TO DRIVE A CAR OR OPERATE MACHINERY, AND MAY CAUSE HEALTH PROBLEMS."
• b. "CONTAINS SULFITES"
• c. "Produced & Bottled by RM Wine Co, Buellton, CA".
• d. Back label copy. T
• "We Love-love cider. Call us crazy, but we feel that cider just might be the bridge between beer-only drinkers and wine-only drinkers - a white flag of sorts. Go on, shake hands. Finally something we can all agree on. Break free from the norm. Drink what you love. Cheers. Nell V."
Nice to have
• 1. OPEN THE "LABELS I LIKE" FILE. Do not submit a design before looking a this file.
• 2. Label must tie in brand name, "Lantern Fall" with a clever prison reference. Prison bars, barbed wire, a shovel, a prison shank, a spoon used to dig a tunnel, a rock pick, a pick-axe, etc.
• 3. Label must tie in apples / apple trees, etc. Something showing what our cider is made of.
• 4. Label must have a memorable font or a logo for brand recognition that will be congruent across all labels.
Should not have
• NO worms in apples please. People do not want to associate or visualize anything like that for food /beverage products.

```html
<!DOCTYPE html>
<html lang="en">
<head>
<meta charset="utf-8">
<title>Lantern Fall – California Hard Apple Cider Label</title>
<link rel="stylesheet" href="https://fonts.googleapis.com/css2?family=Amatic+SC:wght@700&family=Montserrat:wght@500&display=swap">
<style>
  :root {
    --cider-amber: #cf8600;
    --cider-amber-light: #d99a1e;
    --ink: #111111;
    --paper: #ffffff;
    --stripe: #e4e4e4;
  }
  html, body {
    margin: 0;
    padding: 0;
    overflow: hidden;
    background: var(--paper);
  }
  .label {
    position: relative;
    width: 1163px;
    height: 1200px;
    overflow: hidden;
    background:
      repeating-linear-gradient(
        to bottom,
        var(--paper) 0px,
        var(--paper) 17px,
        var(--stripe) 17px,
        var(--stripe) 21px
      );
  }
  .label-art {
    position: absolute;
    inset: 0;
    width: 1163px;
    height: 1200px;
  }
  .brand-name {
    font-family: "Amatic SC", "Trebuchet MS", cursive;
    font-weight: 700;
    fill: var(--paper);
  }
  .product-line {
    font-family: "Amatic SC", "Trebuchet MS", cursive;
    font-weight: 700;
    fill: var(--cider-amber);
  }
  .style-name {
    font-family: "Montserrat", Arial, sans-serif;
    font-weight: 500;
    fill: var(--ink);
  }
  .abv {
    position: absolute;
    left: 30px;
    top: 1124px;
    margin: 0;
    font-family: "Montserrat", Arial, sans-serif;
    font-weight: 500;
    font-size: 38px;
    line-height: 1;
    color: var(--ink);
    letter-spacing: 1px;
    white-space: nowrap;
  }
</style>
</head>
<body>
<main class="label">
  <svg class="label-art" viewBox="0 0 1163 1200" xmlns="http://www.w3.org/2000/svg">
    <defs>
      <path id="product-arc" d="M 140,945 Q 582,790 1030,955" fill="none"/>
    </defs>

    <!-- seal: white disc with double ring -->
    <circle class="seal-disc" cx="582" cy="598" r="552" fill="var(--paper)"/>
    <circle class="seal-ring-outer" cx="582" cy="598" r="552" fill="none" stroke="var(--ink)" stroke-width="5"/>
    <circle class="seal-ring-inner" cx="582" cy="598" r="540" fill="none" stroke="var(--ink)" stroke-width="2"/>

    <!-- tally-mark artwork area -->
    <rect class="tally-marks" role="img" aria-label="Hand-drawn amber tally marks counting days, two crossed groups of five and three single strokes"
          x="350" y="112" width="432" height="300" rx="6" fill="var(--cider-amber)" opacity="0.18"/>

    <!-- name banner -->
    <polygon class="name-banner" points="100,405 588,462 1065,405 1065,812 588,722 100,765" fill="var(--cider-amber)"/>
    <polygon class="name-banner-inset" points="118,425 588,480 1050,425 1050,792 588,705 118,748" fill="none" stroke="var(--cider-amber-light)" stroke-width="6"/>

    <text class="brand-name" x="145" y="665" font-size="215" textLength="888" lengthAdjust="spacingAndGlyphs">LANTERN FALL</text>

    <text class="product-line" font-size="100">
      <textPath href="#product-arc" startOffset="40" textLength="820" lengthAdjust="spacingAndGlyphs">CALIFORNIA HARD APPLE CIDER</textPath>
    </text>

    <!-- style placeholder -->
    <text class="style-name" x="373" y="978" font-size="82">OFF</text>
    <line class="style-divider" x1="628" y1="925" x2="524" y2="1028" stroke="var(--ink)" stroke-width="4" stroke-linecap="round"/>
    <text class="style-name" x="598" y="1058" font-size="82">DRY</text>
  </svg>

  <p class="abv">Alc / Vol 7.0%</p>
</main>
</body>
</html>
```